The Halvard Cabin (Ebook cover design)

Trying to find the perfect ebook cover design for my novel. Its a thriller/horror novel. I like very subtle yet chilling covers. I'll attach some book covers that I love for inspiration.
My book takes place mostly in a large cabin in the middle of the woods during the summer at night. Its also a survival type horror if that helps. I would like the color red or black to be the backdrop. Its for a kindle edition novel, and I'm using word. I would like my name on the top as the author (Marisol Dunkelby) and the title of the novel "The Halvard Cabin" in the middle or bottom, whatever looks best. I'm just looking for something subtle but not too over the top.
Another idea I have is a shovel stuck in the dirt above a open grave with a hand coming out.
Thanks in advance, I appreciate all submissions!
Other font styles liked:
- Copperplate Gothic Light
Requirements
Must have
- Author name and title of book
Nice to have
- Red or black background/ eerie dark setting/ author name and book title in black or red
Should not have
- Bright colors

```html
<!DOCTYPE html>
<html lang="en">
<head>
<meta charset="utf-8">
<title>The Halvard Cabin — Marisol Dunkelby</title>
<link rel="stylesheet" href="https://fonts.googleapis.com/css2?family=Bebas+Neue&family=Playfair+Display:wght@500&display=swap">
<style>
  :root {
    --blood: #cc232c;
    --blood-deep: #5a0b10;
    --ink: #000000;
    --moon: #ffffff;
  }
  html, body {
    margin: 0;
    padding: 0;
    width: 750px;
    height: 1200px;
    overflow: hidden;
    background: var(--ink);
  }
  .cover {
    position: relative;
    width: 750px;
    height: 1200px;
    background: var(--ink);
    overflow: hidden;
  }
  .cover-art,
  .cover-type {
    position: absolute;
    left: 0;
    top: 0;
    width: 750px;
  }
  .cover-art { height: 780px; }
  .cover-type { height: 1200px; }
  .author {
    font-family: "Bebas Neue", "Arial Narrow", sans-serif;
    font-size: 47px;
    fill: var(--ink);
    stroke: var(--ink);
    stroke-width: 1.2px;
    text-transform: uppercase;
  }
  .title {
    font-family: "Playfair Display", "Times New Roman", serif;
    font-weight: 500;
    font-size: 118px;
    fill: var(--blood);
    text-transform: uppercase;
  }
</style>
</head>
<body>
  <main class="cover">
    <svg class="cover-art" role="img" aria-label="Illustration: a dark wooden cabin with glowing red windows in a dense pine forest, silhouetted against a large white full moon on a blood-red night sky, with bats flying" viewBox="0 0 750 780" xmlns="http://www.w3.org/2000/svg">
      <defs>
        <radialGradient id="moon-glow" cx="400" cy="320" r="150" gradientUnits="userSpaceOnUse">
          <stop offset="0" stop-color="var(--moon)"/>
          <stop offset="0.75" stop-color="var(--moon)" stop-opacity="0.9"/>
          <stop offset="1" stop-color="var(--moon)" stop-opacity="0"/>
        </radialGradient>
        <linearGradient id="forest-sides" x1="0" y1="0" x2="1" y2="0">
          <stop offset="0" stop-color="var(--ink)" stop-opacity="0.95"/>
          <stop offset="0.2" stop-color="var(--ink)" stop-opacity="0.7"/>
          <stop offset="0.34" stop-color="var(--ink)" stop-opacity="0"/>
          <stop offset="0.68" stop-color="var(--ink)" stop-opacity="0"/>
          <stop offset="0.82" stop-color="var(--ink)" stop-opacity="0.7"/>
          <stop offset="1" stop-color="var(--ink)" stop-opacity="0.95"/>
        </linearGradient>
        <linearGradient id="ground-fade" x1="0" y1="0" x2="0" y2="1">
          <stop offset="0" stop-color="var(--ink)" stop-opacity="0"/>
          <stop offset="0.5" stop-color="var(--ink)" stop-opacity="0"/>
          <stop offset="0.72" stop-color="var(--ink)" stop-opacity="0.75"/>
          <stop offset="0.92" stop-color="var(--ink)"/>
          <stop offset="1" stop-color="var(--ink)"/>
        </linearGradient>
      </defs>
      <rect width="750" height="780" fill="var(--blood)"/>
      <rect width="750" height="780" fill="url(#moon-glow)"/>
      <rect width="750" height="780" fill="url(#forest-sides)"/>
      <rect width="750" height="780" fill="url(#ground-fade)"/>
    </svg>

    <svg class="cover-type" viewBox="0 0 750 1200" xmlns="http://www.w3.org/2000/svg">
      <text class="author" x="376" y="102" text-anchor="middle">Marisol</text>
      <text class="author" x="376" y="141" text-anchor="middle">Dunkelby</text>

      <text class="title" x="113" y="898" textLength="218" lengthAdjust="spacingAndGlyphs">The</text>
      <text class="title" x="123" y="995" textLength="513" lengthAdjust="spacingAndGlyphs">Halvard</text>
      <text class="title" x="357" y="1089" textLength="279" lengthAdjust="spacingAndGlyphs">Cabin</text>
    </svg>
  </main>
</body>
</html>
```